Lanterne architecture business cards

We are a new company based in New Zealand. We Specialize in High end Luxury Residential Architecture.

Every home is bespoke and is designed to each clients individual requirements and needs.

I like to design buildings that inspire people through light and form while offering a high level of comfort and usability.

Lines of sight, proportion and balance are fundamental to the spaces I create.
Updates

August 5th is current deadline - Today's date is the 13th of August.

Target Market(s)

New Zealanders who want a custom individual home design, typically 30-65 year old males and females

Industry/Entity Type

Architecture

Contact Information for Business Card

Director - Derek Tolson
Contact Number - 0279164073
Email - info@lanternearchitecture-example.co.nz
Webstie - www.lanternearchitecture-example.co.nz
Social Media - @lanternearchitecture

Font styles to use
Sans Serif

Requirements
Must have
• Logo (Both Sides)
Website
Email
Contact Number
Social Media

Nice to have
• Texture
Should not have
• More than 3 colours - typically I would've thought 2 would be good to match the logo.

```html
<!DOCTYPE html>
<html lang="en">
<head>
<meta charset="utf-8">
<title>Lanterne architecture business cards</title>
<link rel="stylesheet" href="https://fonts.googleapis.com/css2?family=Questrial&family=Mulish:wght@400;700&display=swap">
<style>
  :root {
    --ink: #0a0a0a;
    --paper: #ffffff;
    --backdrop: #d1d2d4;
    --muted: #b9b9b9;
    --text: #1a1a1a;
  }
  * { margin: 0; padding: 0; box-sizing: border-box; }
  html, body { width: 1159px; height: 1200px; overflow: hidden; }
  body {
    background: var(--backdrop);
    display: flex;
    flex-direction: column;
    align-items: center;
    justify-content: center;
    gap: 44px;
    font-family: "Questrial", sans-serif;
  }
  .card {
    position: relative;
    width: 920px;
    height: 526px;
    overflow: hidden;
  }
  /* Front */
  .card-front { background: var(--ink); }
  .card-front .stem-band {
    position: absolute; top: 0; bottom: 0;
    left: 72.5%; width: 8%;
    background: var(--paper);
  }
  .brand {
    position: absolute;
    left: 37%; top: 22%;
    transform: translateX(-50%);
    display: flex; flex-direction: column; align-items: center;
    color: var(--paper);
  }
  .brand-dot {
    width: 92px; height: 92px;
    border: 9px solid var(--paper);
    border-radius: 50%;
    margin-bottom: 52px;
  }
  .brand-name {
    font-size: 44px;
    letter-spacing: 0.42em;
    margin-right: -0.42em;
    line-height: 1;
  }
  .brand-sub {
    margin-top: 12px;
    font-size: 11px;
    letter-spacing: 1.45em;
    margin-right: -1.45em;
  }
  /* Back */
  .card-back { background: var(--paper); }
  .card-back .edge-band {
    position: absolute; top: 0; bottom: 0;
    left: 0; width: 4%;
    background: var(--ink);
  }
  .card-back .stem-band {
    position: absolute; top: 0; bottom: 0;
    left: 19%; width: 10%;
    background: var(--ink);
  }
  .person {
    position: absolute; left: 39%; top: 20%;
    font-family: "Mulish", sans-serif;
    color: var(--text);
  }
  .person-name { font-size: 40px; font-weight: 700; line-height: 1.1; }
  .person-role { font-size: 31px; font-weight: 400; line-height: 1.1; }
  .contacts {
    position: absolute; left: 33%; top: 48%;
    list-style: none;
    font-family: "Mulish", sans-serif;
    font-size: 21px;
    color: var(--text);
  }
  .contacts li {
    display: flex; align-items: center; gap: 16px;
    height: 48px;
  }
  .contacts .icon { width: 26px; height: 26px; flex: none; }
  .contacts .social { margin-left: 4px; }
  .mini-brand {
    position: absolute; right: 20px; bottom: 20px;
    display: flex; flex-direction: column; align-items: center;
    color: var(--muted);
  }
  .mini-brand .brand-dot {
    width: 38px; height: 38px; border: 4px solid var(--muted);
    margin-bottom: 18px; align-self: flex-end; margin-right: 60px;
  }
  .mini-brand .brand-name { font-size: 21px; letter-spacing: 0.4em; margin-right: -0.4em; }
  .mini-brand .brand-sub { font-size: 5px; margin-top: 4px; letter-spacing: 1.4em; }
</style>
</head>
<body>

<section class="card card-front" aria-label="Card front">
  <div class="brand">
    <div class="brand-dot"></div>
    <div class="brand-name">LANTERNE</div>
    <div class="brand-sub">ARCHITECTURE</div>
  </div>
  <div class="stem-band"></div>
</section>

<section class="card card-back" aria-label="Card back">
  <div class="edge-band"></div>
  <div class="stem-band"></div>

  <div class="person">
    <p class="person-name">Derek Tolson</p>
    <p class="person-role">Director</p>
  </div>

  <ul class="contacts">
    <li>
      <svg class="icon" viewBox="0 0 26 26" aria-hidden="true">
        <circle cx="13" cy="13" r="13" fill="#0a0a0a"/>
        <path d="M9 7.5c.6-.4 1.3-.3 1.6.3l1.1 2c.3.5.1 1.1-.3 1.4l-.7.5c.6 1.4 1.7 2.5 3.1 3.2l.5-.7c.3-.5.9-.6 1.4-.3l2 1.1c.6.3.7 1 .3 1.6l-.7.9c-.5.6-1.3.8-2 .5-3.2-1.3-5.6-3.7-6.9-6.9-.3-.7-.1-1.5.5-2z" fill="#fff"/>
      </svg>
      <span>0279164073</span>
    </li>
    <li>
      <svg class="icon" viewBox="0 0 26 26" aria-hidden="true">
        <circle cx="13" cy="13" r="13" fill="#0a0a0a"/>
        <g fill="none" stroke="#fff" stroke-width="1.3">
          <circle cx="13" cy="13" r="6"/>
          <ellipse cx="13" cy="13" rx="2.6" ry="6"/>
          <path d="M7 13h12"/>
        </g>
      </svg>
      <span>www.lanternearchitecture-example.co.nz</span>
    </li>
    <li>
      <svg class="icon" viewBox="0 0 26 26" aria-hidden="true">
        <circle cx="13" cy="13" r="13" fill="#0a0a0a"/>
        <rect x="7" y="8.5" width="12" height="9" rx="1" fill="#fff"/>
        <path d="M7.5 9.2l5.5 4.6 5.5-4.6" fill="none" stroke="#0a0a0a" stroke-width="1.2"/>
      </svg>
      <span>info@lanternearchitecture-example.co.nz</span>
    </li>
    <li class="social">Social Media - @lanternearchitecture</li>
  </ul>

  <div class="mini-brand">
    <div class="brand-dot"></div>
    <div class="brand-name">LANTERNE</div>
    <div class="brand-sub">ARCHITECTURE</div>
  </div>
</section>

</body>
</html>
```